Torvin Electrics Flyer Design Advertising

I am after an A5 Flyer design to help promote my electrical services business.
I would like to have information on what my business offers, photos of electrical work, and specials/deals for an amount of time.

Industry/Entity Type

Electrician

Font styles to use
Sans Serif

Colors
0292cd
33a6d7
85cae6
3176b5
333333
1b1b1b
ffffff
5c5c5c
474747

Requirements
Must have
• Specialising in New homes, renovations and commercial projects
• Contact details:
• ph. 0457 613 948
• email admin@torvinelectrics.com.au
• facebook TorvinElectrics
• Specials/Deals:
• 10% off all electrical services
• or
• Free LED downlights on installation
• *Terms conditions apply
• ALL RESIDENTIAL & COMMERCIAL ELECTRICAL SERVICES
• - New Home installations
• - Commercial projects
• - Shop fit outs
• - Renovations
• - Smoke Detectors
• - Air Conditioning and Ceiling Fans
• - Garden Lighting
• - Oven and Cooktop Installations
• - Power Point installation
• - LED lighting upgrades
• - Security Lighting
• - Switchboard upgrades
• - Test and Tag
• - Commercial Property
• - General Electrical Maintenance

```html
<!DOCTYPE html>
<html lang="en">
<head>
<meta charset="utf-8">
<title>Torvin Electrics – Flyer</title>
<link href="https://fonts.googleapis.com/css2?family=League+Gothic&family=Montserrat:wght@500;700;800;900&family=Roboto+Condensed:wght@500&display=swap" rel="stylesheet">
<style>
  :root{
    --brand-blue:#3176b5;
    --sky:#33a6d7;
    --pale-sky:#85cae6;
    --cyan:#0292cd;
    --charcoal:#333333;
    --ink:#1b1b1b;
    --white:#ffffff;
    --grey:#5c5c5c;
    --grey-dark:#474747;
  }
  *{box-sizing:border-box;margin:0;padding:0}
  html,body{width:934px;height:1200px;overflow:hidden;background:var(--white)}
  .flyer{position:relative;width:934px;height:1200px;background:var(--white);font-family:"Montserrat",sans-serif;overflow:hidden}

  /* left column */
  .sidebar{position:absolute;left:0;top:0;width:333px;height:1200px;background:var(--brand-blue);color:var(--white)}
  .sidebar-header{position:absolute;left:0;top:0;width:333px;height:214px}
  .brand{position:absolute;left:30px;top:72px;display:flex;align-items:center;gap:12px}
  .brand-dot{width:58px;height:58px;border-radius:50%;background:var(--sky);flex:none}
  .brand-name{font-family:"Montserrat",sans-serif;font-weight:800;font-size:25px;color:var(--charcoal);letter-spacing:.5px;line-height:1.05;text-transform:uppercase}

  .services-heading{position:absolute;left:27px;top:250px;font-weight:700;font-size:17.5px;line-height:22px;text-transform:uppercase}
  .services-heading .accent{display:block;font-weight:900;font-size:35px;line-height:40px;color:var(--pale-sky);margin-top:2px}

  .service-list{position:absolute;left:25px;top:350px;list-style:none}
  .service-list li{display:flex;align-items:center;height:28.7px;font-family:"Roboto Condensed",sans-serif;font-weight:500;font-size:17px;white-space:nowrap}
  .service-list svg{width:12px;height:12px;margin-right:14px;flex:none}

  .feature-round{position:absolute;left:52px;top:814px;width:222px;height:222px;border-radius:50%;background:var(--white);box-shadow:0 6px 14px rgba(0,0,0,.35);padding:9px}
  .feature-round .photo{width:100%;height:100%;border-radius:50%;background:radial-gradient(circle at 55% 45%,#f4f6f8 0%,#d9e0e4 55%,#7e9a86 100%)}

  .contact{position:absolute;left:29px;top:1062px}
  .contact-title{font-weight:800;font-size:15.5px;text-transform:uppercase;letter-spacing:.2px}
  .contact-row{display:flex;align-items:center;gap:12px}
  .contact-phone{font-weight:800;font-size:33px;line-height:38px;margin-top:2px}
  .contact-mail,.contact-social{font-weight:500;font-size:16.5px;line-height:26px}
  .contact-row svg{flex:none}
  .social-dot{width:20px;height:20px;border-radius:50%;background:var(--white);flex:none}

  /* right column */
  .photo{display:block}
  .photo-hero{position:absolute;left:333px;top:0;width:601px;height:416px;background:linear-gradient(160deg,#3a5d86 0%,#7b7a62 40%,#3f5a33 70%,#23341f 100%)}
  .photo-living{position:absolute;left:338px;top:423px;width:290px;height:178px;background:linear-gradient(180deg,#f1f1ef 0%,#dcd6cc 60%,#a89c8a 100%)}
  .photo-bath{position:absolute;left:636px;top:423px;width:298px;height:178px;background:linear-gradient(120deg,#d7d4d0 0%,#efefee 45%,#8b8a8a 100%)}
  .photo-kitchen{position:absolute;left:691px;top:607px;width:243px;height:153px;background:linear-gradient(180deg,#e7e7e5 0%,#b9b4ad 50%,#6b6560 100%)}
  .photo-open-plan{position:absolute;left:332px;top:1015px;width:309px;height:185px;background:linear-gradient(180deg,#ecebe8 0%,#a9a39b 55%,#4a3a2c 100%)}
  .photo-grey-kitchen{position:absolute;left:650px;top:1015px;width:284px;height:185px;background:linear-gradient(180deg,#f2f2f2 0%,#9a9a9a 55%,#e1e1e1 100%)}

  .headline{position:absolute;left:348px;top:622px;font-family:"League Gothic",sans-serif;font-size:79px;line-height:70px;color:var(--brand-blue);text-transform:uppercase;letter-spacing:.3px}
  .subheadline{position:absolute;left:349px;top:778px;font-weight:800;font-size:26.5px;line-height:29px;color:var(--ink);text-transform:uppercase}

  .deals{position:absolute;left:332px;top:856px;width:602px;height:151px;background:var(--charcoal);color:var(--white)}
  .deals-label{position:absolute;left:21px;top:46px;font-family:"League Gothic",sans-serif;font-size:33px;line-height:29px;text-transform:uppercase}
  .deal-discount{position:absolute;left:136px;top:8px;width:178px;text-align:center}
  .deal-discount .figure{font-weight:900;font-size:74px;line-height:74px;color:var(--sky);letter-spacing:-3px;text-align:left;padding-left:2px}
  .deal-discount .figure sup{font-size:44px;vertical-align:top;position:relative;top:-4px;letter-spacing:0}
  .deal-discount .off{position:absolute;left:105px;top:40px;font-weight:800;font-size:30px;color:var(--white)}
  .deal-discount .small{font-weight:700;font-size:16.5px;line-height:18px;text-transform:uppercase;margin-top:-2px}
  .deal-discount .big{font-weight:800;font-size:27px;line-height:30px;text-transform:uppercase}
  .deal-or{position:absolute;left:320px;top:60px;width:36px;height:36px;border-radius:50%;background:var(--brand-blue);font-weight:800;font-size:13px;display:flex;align-items:center;justify-content:center}
  .deal-free{position:absolute;left:368px;top:16px;width:204px;text-align:center}
  .deal-free .figure{font-weight:900;font-size:68px;line-height:68px;color:var(--sky);letter-spacing:1px}
  .deal-free .lines{font-weight:700;font-size:20px;line-height:23px;text-transform:uppercase;white-space:nowrap}
  .deal-terms{position:absolute;right:36px;bottom:7px;font-size:8px;font-weight:500;text-transform:uppercase;color:#d6d6d6}
</style>
</head>
<body>
<main class="flyer">

  <aside class="sidebar">
    <svg class="sidebar-header" viewBox="0 0 333 214" aria-hidden="true">
      <polygon points="0,0 333,0 333,146 166,213 0,146" fill="#ffffff"/>
    </svg>
    <div class="brand">
      <span class="brand-dot"></span>
      <span class="brand-name">Torvin<br>Electrics</span>
    </div>

    <h2 class="services-heading">All Residential<br>&amp; Commercial Electrical<span class="accent">Services</span></h2>

    <ul class="service-list">
      <li><svg viewBox="0 0 12 12"><circle cx="6" cy="6" r="6" fill="#fff"/><path d="M4.5 3.5 7 6 4.5 8.5" stroke="#3176b5" stroke-width="1.6" fill="none"/></svg>New Home installations</li>
      <li><svg viewBox="0 0 12 12"><circle cx="6" cy="6" r="6" fill="#fff"/><path d="M4.5 3.5 7 6 4.5 8.5" stroke="#3176b5" stroke-width="1.6" fill="none"/></svg>Commercial projects</li>
      <li><svg viewBox="0 0 12 12"><circle cx="6" cy="6" r="6" fill="#fff"/><path d="M4.5 3.5 7 6 4.5 8.5" stroke="#3176b5" stroke-width="1.6" fill="none"/></svg>Shop fit outs</li>
      <li><svg viewBox="0 0 12 12"><circle cx="6" cy="6" r="6" fill="#fff"/><path d="M4.5 3.5 7 6 4.5 8.5" stroke="#3176b5" stroke-width="1.6" fill="none"/></svg>Renovations</li>
      <li><svg viewBox="0 0 12 12"><circle cx="6" cy="6" r="6" fill="#fff"/><path d="M4.5 3.5 7 6 4.5 8.5" stroke="#3176b5" stroke-width="1.6" fill="none"/></svg>Smoke Detectors</li>
      <li><svg viewBox="0 0 12 12"><circle cx="6" cy="6" r="6" fill="#fff"/><path d="M4.5 3.5 7 6 4.5 8.5" stroke="#3176b5" stroke-width="1.6" fill="none"/></svg>Air Conditioning and Ceiling Fans</li>
      <li><svg viewBox="0 0 12 12"><circle cx="6" cy="6" r="6" fill="#fff"/><path d="M4.5 3.5 7 6 4.5 8.5" stroke="#3176b5" stroke-width="1.6" fill="none"/></svg>Garden Lighting</li>
      <li><svg viewBox="0 0 12 12"><circle cx="6" cy="6" r="6" fill="#fff"/><path d="M4.5 3.5 7 6 4.5 8.5" stroke="#3176b5" stroke-width="1.6" fill="none"/></svg>Oven and Cooktop Installations</li>
      <li><svg viewBox="0 0 12 12"><circle cx="6" cy="6" r="6" fill="#fff"/><path d="M4.5 3.5 7 6 4.5 8.5" stroke="#3176b5" stroke-width="1.6" fill="none"/></svg>Power Point installation</li>
      <li><svg viewBox="0 0 12 12"><circle cx="6" cy="6" r="6" fill="#fff"/><path d="M4.5 3.5 7 6 4.5 8.5" stroke="#3176b5" stroke-width="1.6" fill="none"/></svg>LED lighting upgrades</li>
      <li><svg viewBox="0 0 12 12"><circle cx="6" cy="6" r="6" fill="#fff"/><path d="M4.5 3.5 7 6 4.5 8.5" stroke="#3176b5" stroke-width="1.6" fill="none"/></svg>Security Lighting</li>
      <li><svg viewBox="0 0 12 12"><circle cx="6" cy="6" r="6" fill="#fff"/><path d="M4.5 3.5 7 6 4.5 8.5" stroke="#3176b5" stroke-width="1.6" fill="none"/></svg>Switchboard upgrades</li>
      <li><svg viewBox="0 0 12 12"><circle cx="6" cy="6" r="6" fill="#fff"/><path d="M4.5 3.5 7 6 4.5 8.5" stroke="#3176b5" stroke-width="1.6" fill="none"/></svg>Test and Tag</li>
      <li><svg viewBox="0 0 12 12"><circle cx="6" cy="6" r="6" fill="#fff"/><path d="M4.5 3.5 7 6 4.5 8.5" stroke="#3176b5" stroke-width="1.6" fill="none"/></svg>Commercial Property</li>
      <li><svg viewBox="0 0 12 12"><circle cx="6" cy="6" r="6" fill="#fff"/><path d="M4.5 3.5 7 6 4.5 8.5" stroke="#3176b5" stroke-width="1.6" fill="none"/></svg>General Electrical Maintenance</li>
    </ul>

    <div class="feature-round">
      <div class="photo" role="img" aria-label="Photo of a bright white living room with louvre windows opening onto a garden and pool"></div>
    </div>

    <div class="contact">
      <p class="contact-title">Contact Details</p>
      <p class="contact-row contact-phone">
        <svg width="20" height="32" viewBox="0 0 20 32" aria-hidden="true"><rect x="2" y="1.5" width="16" height="29" rx="3" fill="none" stroke="#fff" stroke-width="2.6"/><rect x="6" y="5" width="8" height="18" fill="#fff"/><circle cx="10" cy="26.5" r="1.6" fill="#fff"/></svg>
        0457 613 948
      </p>
      <p class="contact-row contact-mail">
        <svg width="20" height="14" viewBox="0 0 20 14" aria-hidden="true"><rect x="1" y="1" width="18" height="12" fill="none" stroke="#fff" stroke-width="1.8"/><path d="M1 1 10 8 19 1" fill="none" stroke="#fff" stroke-width="1.8"/></svg>
        admin@torvinelectrics.com.au
      </p>
      <p class="contact-row contact-social"><span class="social-dot"></span>TorvinElectrics</p>
    </div>
  </aside>

  <div class="photo photo-hero" role="img" aria-label="Photo of a modern two-storey home at dusk with a lit covered patio, lounge and lush tropical garden beside a pool"></div>
  <div class="photo photo-living" role="img" aria-label="Photo of an open living room with white sofas, artwork and ceiling fan"></div>
  <div class="photo photo-bath" role="img" aria-label="Photo of a modern bathroom with glass shower, large mirror and downlights"></div>
  <div class="photo photo-kitchen" role="img" aria-label="Photo of a contemporary kitchen with pendant lights over the island"></div>

  <h1 class="headline">Specialising<br>in new homes</h1>
  <p class="subheadline">Renovations and<br>commercial projects</p>

  <section class="deals">
    <p class="deals-label">Specials<br>deals:</p>
    <div class="deal-discount">
      <p class="figure">10<sup>%</sup></p>
      <span class="off">OFF</span>
      <p class="small">All electrical</p>
      <p class="big">Services</p>
    </div>
    <span class="deal-or">OR</span>
    <div class="deal-free">
      <p class="figure">FREE</p>
      <p class="lines">LED downlights<br>on installation</p>
    </div>
    <p class="deal-terms">*Terms conditions apply</p>
  </section>

  <div class="photo photo-open-plan" role="img" aria-label="Photo of an open-plan kitchen and living area with timber floor and downlights"></div>
  <div class="photo photo-grey-kitchen" role="img" aria-label="Photo of a grey modern kitchen with fridge, island bench and pendant lights"></div>

</main>
</body>
</html>
```